Web design for Money Service Business (uncoded)

We need a very basic website with 5-6 pages. Home page, Services, Transfer(How to use our service), About us, Contact us, FAQ
Our company name is Harbin Coinage. We are a company that deals with currency exchange and international money transfer. We do cash exchange and international money transfers to bank accounts all over the world. We offer highly competitive exchange rates so usually attract customers who transfer money over $10,000. Our niche is with larger sums of money, the design needs to be professional and communicate trust, security and stability.
Industry/Entity Type
Security
Look and feel
Each slider illustrates characteristics of the customer's brand and the style your logo design should communicate.

```html
<!DOCTYPE html>
<html lang="en">
<head>
<meta charset="utf-8">
<title>Harbin Coinage — International Money Transfer</title>
<link rel="stylesheet" href="https://fonts.googleapis.com/css2?family=Open+Sans:ital,wght@0,400;0,600;0,700;1,400&family=Merriweather:wght@400&display=swap">
<style>
:root{
  --blue:#1a5488;
  --blue-dark:#154a79;
  --orange:#f38b0f;
  --ink:#2b2b2b;
  --muted:#555;
  --hero-bg:#f2f2f2;
  --line:#e2e2e2;
  --white:#fff;
}
*{margin:0;padding:0;box-sizing:border-box}
html,body{width:904px;height:1200px;overflow:hidden;background:var(--white)}
body{position:relative;font-family:"Open Sans",Arial,sans-serif;color:var(--ink)}
.abs{position:absolute}
.top-strip{left:0;top:0;width:904px;height:5px;background:var(--blue)}
.brand{left:100px;top:36px;display:flex;align-items:center;gap:7px;font-weight:700;font-size:19px;color:var(--blue);letter-spacing:.5px}
.brand-dot{width:12px;height:12px;border-radius:50%;background:var(--orange)}
.nav-home{left:450px;top:7px;width:78px;height:89px;background:#f3f3f3;border-bottom:4px solid var(--orange)}
.nav a{position:absolute;top:44px;font-size:11.5px;color:#444;text-decoration:none}
.nav a.active{color:var(--blue)}
.hero{left:0;top:96px;width:904px;height:332px;background:repeating-linear-gradient(135deg,#f4f4f4 0 2px,#efefef 2px 4px)}
.hero-shade{left:98px;top:96px;width:708px;height:28px;background:radial-gradient(ellipse at top,rgba(0,0,0,.13),rgba(0,0,0,0) 70%)}
.hero-title{left:99px;top:162px;font-size:16.5px;color:var(--blue);font-weight:400}
.hero-sub{left:99px;top:185px;font-size:16.5px;color:#1c1c1c}
.hero-tag{left:99px;top:210px;font-size:12px;color:var(--orange);font-weight:600}
.hero-copy{left:99px;top:241px;width:280px;font-size:9.2px;line-height:15px;font-weight:600;color:#333}
.btn-blue{background:var(--blue);color:#fff;border-radius:3px;font-size:11px;font-weight:600;display:flex;align-items:center;justify-content:center}
.hero-btn{left:98px;top:321px;width:104px;height:27px}
.slider{left:391px;top:146px;width:416px;height:232px;background:linear-gradient(135deg,#5d5a4f,#8d8c7d 45%,#4a3d35 70%,#9a9b8b);box-shadow:0 3px 6px rgba(0,0,0,.35)}
.slide-arrow{width:31px;height:31px;background:rgba(20,20,20,.8);top:248px}
.services .svc{position:absolute;top:468px;width:230px}
.svc-icon{position:absolute;left:0;top:0;width:48px;height:48px;border-radius:50%;background:var(--blue)}
.svc h3{position:absolute;left:54px;top:6px;font-family:"Merriweather",Georgia,serif;font-weight:400;font-size:14px;color:var(--orange);white-space:nowrap}
.svc p{position:absolute;left:57px;top:27px;width:175px;font-size:8.8px;line-height:13.5px;color:#444}
.svc a{position:absolute;left:57px;top:69px;font-size:9px;font-weight:600;color:var(--blue);text-decoration:none;white-space:nowrap}
.offer{left:98px;top:588px;width:709px;height:92px;background:#f6f6f6;border:1px solid var(--line);border-top:6px solid var(--orange)}
.offer-shade{left:98px;top:680px;width:709px;height:26px;background:radial-gradient(ellipse at top,rgba(0,0,0,.12),rgba(0,0,0,0) 70%)}
.offer-ring{left:106px;top:607px;width:54px;height:54px;border-radius:50%;border:2px solid var(--orange);background:#fff}
.offer-copy{left:176px;top:614px;width:480px;font-size:8.8px;line-height:14.5px;color:#333}
.offer-btn{left:666px;top:622px;width:130px;height:27px;font-size:9.5px;font-weight:400}
.sec-head{font-family:"Merriweather",Georgia,serif;font-size:14px;color:var(--blue);white-space:nowrap}
.rule{height:1px;background:var(--line)}
.news-img{top:762px;width:227px;height:88px}
.news-ico{top:859px;width:36px;height:54px}
.news h4{position:absolute;font-size:11px;font-weight:600;color:#222;white-space:nowrap}
.news .meta{position:absolute;font-size:9px;color:var(--orange);white-space:nowrap}
.news p{position:absolute;font-size:8.8px;color:#333;white-space:nowrap}
.news .more{position:absolute;font-size:8.8px;white-space:nowrap}
.quote-box{left:582px;top:762px;width:225px;height:142px;border:1px solid #ddd;background:#fff}
.quote-text{left:607px;top:776px;width:185px;font-size:8.6px;line-height:13px;font-style:italic;color:#333}
.avatar{left:596px;top:852px;width:76px;height:76px;border-radius:50%;background:#fff;box-shadow:0 1px 4px rgba(0,0,0,.25)}
.avatar-fill{left:602px;top:858px;width:64px;height:64px;border-radius:50%;background:radial-gradient(circle at 50% 40%,#d9a883,#8a6a52 60%,#4b8fa8)}
.q-name{left:681px;top:860px;font-size:11.5px;font-weight:700;color:#222}
.q-role{left:681px;top:874px;font-size:10.5px;font-weight:700;color:#aaa}
.footer{left:0;top:996px;width:904px;height:168px;background:var(--blue)}
.hello{left:241px;top:959px;width:78px;height:78px;border-radius:50%;background:var(--orange);color:#fff;font-size:13px;display:flex;align-items:center;justify-content:center}
.f-head{font-size:14px;color:#fff;white-space:nowrap}
.f-item{top:1077px;display:flex;align-items:center;gap:8px;font-size:9.5px;color:#fff;white-space:nowrap}
.f-links{left:98px;top:1110px;font-size:9.5px;color:#fff;white-space:nowrap}
.news-input{left:638px;top:1072px;width:169px;height:27px;background:#fff;border-radius:2px;font-size:9.5px;color:#333;padding-left:8px;display:flex;align-items:center}
.join{left:638px;top:1114px;width:83px;height:21px;background:var(--orange);border-radius:2px;color:#fff;font-size:8px;display:flex;align-items:center;justify-content:center}
.bottom{left:0;top:1164px;width:904px;height:36px;background:var(--orange);font-size:9.2px;color:#222}
.bottom span{position:absolute;top:12px;white-space:nowrap}
</style>
</head>
<body>
<div class="abs top-strip"></div>

<header>
  <div class="abs brand"><span class="brand-dot"></span>HARBIN COINAGE</div>
  <div class="abs nav-home"></div>
  <nav class="nav">
    <a class="active" style="left:473px">HOME</a>
    <a style="left:551px">ABOUT US</a>
    <a style="left:649px">PORTFOLIO</a>
    <a style="left:753px">CONTACT</a>
  </nav>
</header>

<section>
  <div class="abs hero"></div>
  <div class="abs hero-shade"></div>
  <h1 class="abs hero-title">THE HARBIN COINAGE</h1>
  <h2 class="abs hero-sub" style="font-weight:400">INTERNATIONAL MONEY TRANSFER</h2>
  <p class="abs hero-tag">ENSURE THE MONEY TRANSFER IN SAVE HANDS</p>
  <p class="abs hero-copy">Lorem Ipsum est simplement du faux texte employé dans la sition et la misen page avant impression...Lorem Ipsum est simplement du faux texte employé dans la sition et la misen page avant impression...</p>
  <div class="abs btn-blue hero-btn">READ MORE</div>
  <div class="abs slider" role="img" aria-label="Photo of handcuffs lying on banknotes"></div>
  <div class="abs slide-arrow" style="left:391px"><svg width="31" height="31"><path d="M18 9 L12 15.5 L18 22" stroke="#fff" stroke-width="3" fill="none"/></svg></div>
  <div class="abs slide-arrow" style="left:776px"><svg width="31" height="31"><path d="M13 9 L19 15.5 L13 22" stroke="#fff" stroke-width="3" fill="none"/></svg></div>
</section>

<section class="services">
  <div class="svc" style="left:98px">
    <div class="svc-icon"><svg width="48" height="48"><rect x="13" y="17" width="22" height="14" rx="1" fill="none" stroke="#fff" stroke-width="2" transform="rotate(-15 24 24)"/><circle cx="24" cy="24" r="3.5" fill="none" stroke="#fff" stroke-width="1.6"/></svg></div>
    <h3>Currency Exchange</h3>
    <p>Lorem Ipsum est simplement du faux exte mployé dans la sition et la misen page avant impression...</p>
    <a>Read More <svg width="18" height="8"><path d="M0 4H15M11 1L16 4L11 7" stroke="#1a5488" stroke-width="1.4" fill="none"/></svg></a>
  </div>
  <div class="svc" style="left:340px">
    <div class="svc-icon"><svg width="48" height="48"><rect x="18" y="13" width="12" height="21" rx="2" fill="none" stroke="#fff" stroke-width="2" transform="rotate(30 24 24)"/><path d="M12 18a13 13 0 0 0 0 12M36 18a13 13 0 0 1 0 12" stroke="#fff" stroke-width="1.6" fill="none"/></svg></div>
    <h3>Mobile Money Transfer</h3>
    <p>Lorem Ipsum est simplement du faux exte mployé dans la sition et la misen page avant impression...</p>
    <a>Read More <svg width="18" height="8"><path d="M0 4H15M11 1L16 4L11 7" stroke="#1a5488" stroke-width="1.4" fill="none"/></svg></a>
  </div>
  <div class="svc" style="left:583px">
    <div class="svc-icon"><svg width="48" height="48"><rect x="14" y="18" width="22" height="13" rx="2" fill="#fff"/><rect x="14" y="21" width="22" height="3" fill="#1a5488"/><rect x="11" y="22" width="10" height="9" rx="2" fill="none" stroke="#fff" stroke-width="1.6"/></svg></div>
    <h3>Cash To Card</h3>
    <p>Lorem Ipsum est simplement du faux exte mployé dans la sition et la misen page avant impression...</p>
    <a>Read More <svg width="18" height="8"><path d="M0 4H15M11 1L16 4L11 7" stroke="#1a5488" stroke-width="1.4" fill="none"/></svg></a>
  </div>
</section>

<section>
  <div class="abs offer"></div>
  <div class="abs offer-shade"></div>
  <div class="abs offer-ring"><svg width="50" height="50"><path d="M15 25 L25 15 L35 15 L35 25 L25 35 Z" fill="none" stroke="#1a5488" stroke-width="2.2" stroke-linejoin="round"/><circle cx="30" cy="20" r="1.8" fill="#1a5488"/><text x="19" y="29" font-size="9" font-weight="700" fill="#1a5488" font-family="Open Sans,sans-serif">%</text></svg></div>
  <p class="abs offer-copy">Lorem Ipsum est simplement du faux exte mployé dans la ion et la misen page avant impression...dans la ion et la misen page avant impression... Lorem Ipsum est simplement du faux exte mployé dans la ion et la misen page avant impression...dans la ion et la misen page avant impression...</p>
  <div class="abs btn-blue offer-btn">Get A Discount Here</div>
</section>

<section class="news">
  <h2 class="abs sec-head" style="left:98px;top:725px">Latest News</h2>
  <div class="abs rule" style="left:188px;top:734px;width:379px"></div>
  <div class="abs news-img" style="left:98px" role="img" aria-label="Photo of pound sterling banknotes" ></div>
  <div class="abs news-img" style="left:98px;background:linear-gradient(135deg,#c9a99a,#e6d2c4 50%,#9d8c95)"></div>
  <div class="abs news-img" style="left:339px;background:linear-gradient(135deg,#9ea59a,#d7dbd0 50%,#7f8a7f)" role="img" aria-label="Photo of a pile of dollar banknotes"></div>

  <div class="abs news-ico" style="left:98px;background:var(--blue)"><svg width="36" height="54"><rect x="10" y="22" width="16" height="12" rx="1.5" fill="none" stroke="#fff" stroke-width="1.5"/><path d="M13 26H23M13 29H23M14 18L18 22L22 18" stroke="#fff" stroke-width="1.3" fill="none"/></svg></div>
  <h4 style="left:150px;top:857px">Lorem Ipsum est simplement</h4>
  <span class="meta" style="left:149px;top:872px">Dec 12,2013 | by Owen | 13 Comments</span>
  <p style="left:150px;top:890px">Lorem Ipsum est simplement du faux exte</p>
  <span class="more" style="left:150px;top:903px;color:var(--blue)">More&gt;&gt;</span>

  <div class="abs news-ico" style="left:339px;background:var(--orange)"><svg width="36" height="54"><rect x="10" y="22" width="16" height="12" rx="1.5" fill="none" stroke="#fff" stroke-width="1.5"/><path d="M13 26H23M13 29H23M14 18L18 22L22 18" stroke="#fff" stroke-width="1.3" fill="none"/></svg></div>
  <h4 style="left:392px;top:857px">Lorem Ipsum est simplement</h4>
  <span class="meta" style="left:391px;top:872px">Dec 12,2013 | by Owen | 13 Comments</span>
  <p style="left:392px;top:890px">Lorem Ipsum est simplement du faux exte</p>
  <span class="more" style="left:392px;top:903px;color:var(--orange)">More&gt;&gt;</span>
</section>

<section>
  <h2 class="abs sec-head" style="left:581px;top:725px">Testimonial</h2>
  <div class="abs rule" style="left:671px;top:734px;width:108px"></div>
  <div class="abs quote-box"></div>
  <p class="abs quote-text">Lorem Ipsum est simplement du faux exte mployé dans la sition et la misen page avant impression...Lorem Ipsum est simplement du faux exte mployé dans la sition et la misen page avant impression...</p>
  <svg class="abs" style="left:757px;top:852px" width="38" height="30"><path d="M4 0h12v14l-6 14h-6l5-12h-5zM22 0h12v14l-6 14h-6l5-12h-5z" fill="#ececec"/></svg>
  <div class="abs avatar"></div>
  <svg class="abs" style="left:628px;top:926px" width="12" height="7"><path d="M0 0L6 6L12 0Z" fill="#fff"/></svg>
  <div class="abs avatar-fill" role="img" aria-label="Portrait photo of the client giving the testimonial"></div>
  <span class="abs q-name">Daniel Marsh</span>
  <span class="abs q-role">Manager</span>
</section>

<footer>
  <div class="abs footer"></div>
  <div class="abs hello">Hello!</div>
  <svg class="abs" style="left:253px;top:1028px" width="16" height="14"><path d="M0 12L14 0L16 8Z" fill="var(--orange)"/></svg>
  <h2 class="abs f-head" style="left:99px;top:1037px;font-weight:400">Contact Information</h2>
  <h2 class="abs f-head" style="left:634px;top:1037px;font-weight:400">Newsletter subscription</h2>

  <div class="abs f-item" style="left:98px"><svg width="20" height="16"><rect x="1" y="2" width="18" height="13" fill="none" stroke="#fff" stroke-width="1.5"/><circle cx="6" cy="7" r="2" fill="#fff"/><path d="M3 13c0-3 6-3 6 0M11 6h6M11 9h6M11 12h4" stroke="#fff" stroke-width="1.3"/></svg>12 Lantern Row, AUS</div>
  <div class="abs f-item" style="left:250px"><svg width="12" height="18"><path d="M6 17C2 11 1 9 1 6a5 5 0 0 1 10 0c0 3-1 5-5 11z" fill="#fff"/><circle cx="6" cy="6" r="2" fill="var(--blue)"/></svg>555-210-4407</div>
  <div class="abs f-item" style="left:336px"><svg width="20" height="16"><path d="M1 6L10 12L19 6V15H1Z" fill="#fff"/><path d="M5 8V1H15V8" stroke="#fff" stroke-width="1.4" fill="none"/></svg>hello@harbincoinage.com</div>
  <div class="abs f-item" style="left:484px"><svg width="20" height="18"><rect x="1" y="3" width="15" height="13" fill="none" stroke="#fff" stroke-width="1.5"/><path d="M1 7H16" stroke="#fff" stroke-width="1.5"/><circle cx="15" cy="13" r="4.5" fill="#fff"/><path d="M15 11v2.5h2" stroke="var(--blue)" stroke-width="1.2" fill="none"/></svg>From 10:15 Am to 7:30 PM</div>
  <div class="abs f-links">Privacy Policy &nbsp;&nbsp;| &nbsp;&nbsp;&nbsp;FAQS</div>

  <div class="abs news-input">Enter your email address</div>
  <div class="abs join">JOIN US</div>

  <div class="abs bottom">
    <span style="left:98px">Copyright © 2013 Harbin Coinage ltd All Rights Reserved</span>
    <span style="left:632px">Terms &amp; Condition</span>
    <span style="left:729px">|</span>
    <span style="left:751px">Privacy Policy</span>
  </div>
</footer>
</body>
</html>
```